BUSINESS CARD MIRELLE CAVANOSI

I need a new business card for my personal business.
I am a Naturopath and Nutritionist working doing private consults in the health and wellness arena.
I would like to see designs that are, clean minimalist but colourful.
I like:
White (clean,fresh, minimalist)
pops of one colour ONLY.Choose a colour to run with and keep it simple.
green
light blue
mustard
Bright yellow
Charcoal
The final design should communicate professionalism but also be in touch with nature.
Key Information to include:
MIRELLE CAVANOSI
ABN 48 217 603 915
RQTLBE 327081
Tel 0487 639 142
NATUROPATH | HERBALIST | NUTRITON CONSULTANT
BHSc (Naturopathic Studies) Grad Dip (Naturopathy)
BACK OF CARD : YOUR NEXT APPOINTMENT ..................................
I already have a logo (picture attached)But I would be more than happy to NOT have this included. I am very Open to cards WITHOUT current logo/ ones that weave the colour of my logo but do not use the logo.
I have included pictures attached to give examples of the styles/colors I enjoy.
Updates
I have added a picture of a mortar and pestle - one just like this would be lovely to include in your entry.
TIA

```html
<!DOCTYPE html>
<html lang="en">
<head>
<meta charset="utf-8">
<title>Mirelle Cavanosi Naturopathy – Business Cards</title>
<link rel="stylesheet" href="https://fonts.googleapis.com/css2?family=Dosis:wght@300;400;500&display=swap">
<style>
  :root {
    --backdrop: #ece8e2;
    --card-white: #ffffff;
    --green-light: #9ad14a;
    --green-mid: #7cc232;
    --green-deep: #5ea823;
    --green-ink: #3d5a1f;
    --cream-yellow: #f2ef7c;
    --leaf-tint: #dfead0;
    --leaf-tint-soft: #eef4e6;
    --charcoal: #3b3b3b;
    --grey-text: #6b6b6b;
    --accent-orange: #eea23c;
  }
  * { margin: 0; padding: 0; box-sizing: border-box; }
  html, body {
    width: 1200px; height: 913px; overflow: hidden;
    background: var(--backdrop);
    font-family: "Dosis", "Trebuchet MS", sans-serif;
  }
  .canvas {
    position: relative; width: 1200px; height: 913px;
    display: flex; align-items: center; justify-content: center; gap: 40px;
  }
  .card {
    position: relative; width: 540px; height: 309px; overflow: hidden;
    box-shadow: 0 6px 18px rgba(0,0,0,.18);
  }

  /* ---------- Back: qualifications ---------- */
  .card--back {
    background: linear-gradient(150deg, var(--green-light) 0%, var(--green-mid) 50%, var(--green-deep) 100%);
  }
  .card--back .foliage {
    position: absolute; left: 20px; top: 70px; width: 230px; height: 239px;
    background: radial-gradient(ellipse at 45% 55%, rgba(255,255,255,.16), rgba(255,255,255,0) 70%);
  }
  .card--back .brand {
    position: absolute; right: 30px; top: 30px; text-align: right;
    color: var(--green-ink); font-weight: 400; letter-spacing: 4px; font-size: 15px; line-height: 1.35;
  }
  .card--back .brand-mark {
    display: inline-block; width: 20px; height: 20px; border-radius: 50%;
    background: var(--cream-yellow); margin-top: 8px;
  }
  .qualification {
    position: absolute; left: 34px; color: var(--cream-yellow); font-weight: 400; line-height: 1;
  }
  .qualification .title { font-size: 38px; }
  .qualification .field { font-size: 17px; margin-top: 4px; font-weight: 300; }
  .qualification--grad { top: 150px; }
  .qualification--bhsc { top: 222px; left: 112px; }

  /* ---------- Front: contact ---------- */
  .card--front { background: var(--card-white); }
  .card--front .foliage {
    position: absolute; left: 0; top: 90px; width: 250px; height: 219px;
    background: radial-gradient(ellipse at 40% 55%, var(--leaf-tint) 0%, var(--leaf-tint-soft) 50%, rgba(255,255,255,0) 75%);
  }
  .lockup {
    position: absolute; left: 150px; top: 30px; display: flex; align-items: center; gap: 14px;
  }
  .lockup .brand-mark {
    width: 30px; height: 30px; border-radius: 50%; background: var(--accent-orange);
  }
  .lockup .name {
    font-size: 20px; letter-spacing: 5px; color: var(--grey-text); font-weight: 400; line-height: 1.2;
  }
  .lockup .practice {
    font-size: 20px; letter-spacing: 7px; color: var(--accent-orange); font-weight: 300; line-height: 1.2;
  }
  .registrations {
    position: absolute; right: 34px; top: 104px; text-align: right;
    font-size: 16px; letter-spacing: 1px; color: var(--charcoal); line-height: 1.45;
  }
  .services {
    position: absolute; left: 30px; right: 20px; bottom: 28px;
    font-size: 14px; letter-spacing: 1px; color: var(--charcoal); font-weight: 500;
  }
  .services .divider { color: var(--accent-orange); margin: 0 5px; }
</style>
</head>
<body>
<main class="canvas">

  <section class="card card--back" aria-label="Card back with qualifications">
    <div class="foliage" role="img" aria-label="Faint leafy branch illustration"></div>
    <div class="brand">
      <div>MIRELLE CAVANOSI</div>
      <div>NATUROPATHY</div>
      <span class="brand-mark" aria-hidden="true"></span>
    </div>
    <div class="qualification qualification--grad">
      <div class="title">Grad Dip</div>
      <div class="field">(Naturopathy)</div>
    </div>
    <div class="qualification qualification--bhsc">
      <div class="title">BHSc</div>
      <div class="field">(Naturopathic Studies)</div>
    </div>
  </section>

  <section class="card card--front" aria-label="Card front with contact details">
    <div class="foliage" role="img" aria-label="Soft green leafy branch illustration"></div>
    <div class="lockup">
      <span class="brand-mark" aria-hidden="true"></span>
      <div>
        <div class="name">MIRELLE CAVANOSI</div>
        <div class="practice">NATUROPATHY</div>
      </div>
    </div>
    <div class="registrations">
      <div>ABN 48 217 603 915</div>
      <div>RQTLBE 327081</div>
    </div>
    <div class="services">
      NATUROPATH<span class="divider">|</span>HERBALIST<span class="divider">|</span>NUTRITON CONSULTANT
    </div>
  </section>

</main>
</body>
</html>
```